■依頼目的 / 概要
電子書籍Lumora本を出版いたしますので、
表紙デザイン作成をお願いいたします。

■納品物
下記での納品をお願い致します。

JPEG形式 及び PSD形式
横1600ピクセル x 縦2560ピクセル

■本の内容

<本のタイトル>
雑貨長者の資金調達術 〜開業ローン篇〜

<サブタイトル>
会社をつくる お金を借りる 原資ができる

<キャッチコピー>
貯金してから起業なんて絶対ダメ!

<著者名>
早川蒼一

■デザイン要望
・本のタイトル / キャッチコピー / 著者名の反映をお願いします

デザインイメージ

・人物や風景の画像を背景にしていただき、
その上にタイトル等コピーを記載

・シンプルな背景にタイトル等のコピーを記載

・資産形成に関する指南書。
その第一歩である新規創業融資に
焦点を当てた内容になっていますが、
お金に関することだけではなく、
人間関係や人生設計にまで
踏み込んだ内容になっています。

・楽して稼ぐといったレベルの低いイメージをもたせるような
デザインにはしたくありません。

<表現したいイメージなど>
・高級感
・かっこいい
・信頼感

<表現したくないイメージ>
・安っぽい
・嘘くさい
・大衆的

<利用画像について>
画像素材を使用される場合には、
商用利用可の素材をお願いします。

■その他
デザインを考えるのに必要な情報が他にございましたら、
お答えしますので、遠慮なくご連絡ください。

数あるご提案の中で、もっとも世界観を表現していただいているものを当選に選ばせていただきました。

この度は、たくさんのご提案ありがとうございました。
レベルの高いご提案が多く、非常に良いデザインを得ることができました。
今回、ご縁がなかったデザイナー様。また次回、ご提案いただければ幸いです。
ありがとうございました!

```html
<!DOCTYPE html>
<html lang="ja">
<head>
<meta charset="utf-8">
<title>雑貨長者の資金調達術 〜開業ローン篇〜</title>
<link href="https://fonts.googleapis.com/css2?family=Noto+Sans+JP:wght@700;900&family=Noto+Serif+JP:wght@700;900&display=swap" rel="stylesheet">
<style>
  :root {
    --ink: #0b0906;
    --panel: #14100b;
    --gold: #c9a35a;
    --gold-light: #f2d88e;
    --gold-deep: #8a6a2e;
    --yellow: #ffe24a;
    --white: #ffffff;
    --red: #d4141c;
  }
  html, body { margin: 0; padding: 0; overflow: hidden; background: var(--ink); }
  .cover {
    position: relative;
    width: 750px; height: 1200px;
    overflow: hidden;
    background: radial-gradient(ellipse at 50% 35%, #1d1710 0%, var(--ink) 70%);
    font-family: "Noto Sans JP", sans-serif;
  }
  .cover p, .cover h1 { margin: 0; line-height: 1; white-space: nowrap; }
  .frame-art { position: absolute; inset: 0; }
  .series-line {
    position: absolute; top: 92px; left: 0; width: 100%;
    text-align: center;
    font-family: "Noto Serif JP", serif; font-weight: 900;
    font-size: 60px; letter-spacing: 2px;
    color: var(--gold-light);
    text-shadow: 0 2px 0 var(--gold-deep);
  }
  .title {
    position: absolute; left: 0; width: 100%;
    text-align: center; color: var(--white);
    font-weight: 900;
  }
  .title-main { top: 205px; font-size: 140px; letter-spacing: 4px; }
  .title-sub { top: 360px; font-size: 140px; letter-spacing: 8px; }
  .edition-ribbon {
    position: absolute; top: 568px; left: 225px; width: 300px; height: 66px;
  }
  .edition-ribbon span {
    position: absolute; inset: 0;
    display: flex; align-items: center; justify-content: center;
    font-family: "Noto Serif JP", serif; font-weight: 900;
    font-size: 38px; letter-spacing: 3px; color: #1a1208;
    white-space: nowrap;
  }
  .author {
    position: absolute; top: 648px; right: 128px;
    font-family: "Noto Serif JP", serif; font-weight: 700;
    font-size: 30px; letter-spacing: 4px; color: var(--white);
  }
  .steps { position: absolute; inset: 0; margin: 0; padding: 0; list-style: none; }
  .step {
    position: absolute; height: 58px; width: 330px;
    box-sizing: border-box;
    border: 4px solid var(--gold);
    background: var(--panel);
    display: flex; align-items: center; justify-content: center;
    font-weight: 900; font-size: 44px; line-height: 1; letter-spacing: 1px;
    color: var(--yellow); white-space: nowrap;
  }
  .step-1 { top: 692px; left: 100px; }
  .step-2 { top: 764px; left: 208px; }
  .step-3 { top: 836px; left: 316px; }
  .catch-band {
    position: absolute; left: 0; top: 924px; width: 100%; height: 276px;
    background: linear-gradient(180deg, #e9cf86 0%, #c9a35a 45%, #a9823e 100%);
    border-top: 6px solid var(--gold-light);
    box-sizing: border-box;
  }
  .catch-lead {
    position: absolute; top: 24px; left: 0; width: 100%;
    text-align: center; font-weight: 900; font-size: 62px;
    letter-spacing: 1px; color: #0d0a06;
  }
  .catch-punch {
    position: absolute; top: 112px; left: 0; width: 100%;
    text-align: center; font-family: "Noto Serif JP", serif; font-weight: 900;
    font-size: 118px; letter-spacing: 4px; color: var(--red);
    text-shadow: 3px 3px 0 rgba(255,255,255,.6);
  }
</style>
</head>
<body>
<main class="cover">
  <svg class="frame-art" width="750" height="1200" viewBox="0 0 750 1200" aria-hidden="true">
    <defs>
      <linearGradient id="goldLine" x1="0" y1="0" x2="1" y2="1">
        <stop offset="0" stop-color="#f2d88e"/>
        <stop offset=".5" stop-color="#c9a35a"/>
        <stop offset="1" stop-color="#8a6a2e"/>
      </linearGradient>
      <radialGradient id="cornerGlow" cx=".5" cy=".5" r=".5">
        <stop offset="0" stop-color="#8a6a2e" stop-opacity=".55"/>
        <stop offset="1" stop-color="#8a6a2e" stop-opacity="0"/>
      </radialGradient>
    </defs>
    <rect x="22" y="22" width="706" height="890" fill="none" stroke="url(#goldLine)" stroke-width="6"/>
    <rect x="40" y="40" width="670" height="854" fill="none" stroke="url(#goldLine)" stroke-width="2"/>
    <rect x="70" y="185" width="610" height="365" fill="none" stroke="#8a6a2e" stroke-width="2"/>
    <g role="img" aria-label="金色の装飾コーナー模様">
      <circle cx="70" cy="70" r="60" fill="url(#cornerGlow)"/>
      <circle cx="680" cy="70" r="60" fill="url(#cornerGlow)"/>
      <circle cx="70" cy="864" r="60" fill="url(#cornerGlow)"/>
      <circle cx="680" cy="864" r="60" fill="url(#cornerGlow)"/>
    </g>
  </svg>

  <p class="series-line">雑貨長者の</p>
  <h1 class="title title-main">資金調達</h1>
  <h1 class="title title-sub">術</h1>

  <div class="edition-ribbon">
    <svg width="300" height="66" viewBox="0 0 300 66" aria-hidden="true">
      <defs>
        <linearGradient id="ribbonFill" x1="0" y1="0" x2="0" y2="1">
          <stop offset="0" stop-color="#f5e3a8"/>
          <stop offset=".5" stop-color="#d4b06a"/>
          <stop offset="1" stop-color="#a9823e"/>
        </linearGradient>
      </defs>
      <path d="M0 8 H300 L283 33 L300 58 H0 L17 33 Z" fill="url(#ribbonFill)" stroke="#6e5222" stroke-width="2"/>
    </svg>
    <span>開業ローン篇</span>
  </div>

  <p class="author">早川蒼一</p>

  <ul class="steps">
    <li class="step step-1">会社をつくる</li>
    <li class="step step-2">お金を借りる</li>
    <li class="step step-3">原資ができる</li>
  </ul>

  <section class="catch-band">
    <p class="catch-lead">貯金してから起業なんて</p>
    <p class="catch-punch">絶対ダメ!</p>
  </section>
</main>
</body>
</html>
```